Im want a website LIKE KMT's and FleetStride.com's with product payment options like Wendaro's

I need a website LIKE KMT with a header made EXACTLY LIKE THAT OF FLEETSTRIDES .

The front page photo should be like that of FLEETSTRIDE's webpage as well.

The name of the website will be called "C.M. (Calmira Mesa)".

We will be targeting ALL MARKETS in a small town in central Panama and charging businesses "listing fees" like a phone book does but also providing informational blogs, news, and other interesting activities.

THIS IS A MULTI PAGE WEBSITE

THIS IS WHERE KMT's website meets Norvex/FleetStride.

Once the layout is built I will tweak and modify, add information, and upload items for sale.

Here is a list of specific categories that should be listed out above the front page header image/search bar

-- Home -- News -- Travel -- Activities -- Shop & Dine -- Store -- More... --

These categories should be spread across the bottom of the page in three sections:

WHATS SO GREAT ABOUT (Calmira Mesa),
HAND PICKED TOURS
ACTIVITIES etc.

Also lets use www.Wendaro.example 's
"HOT DESTINATIONS"
"BEAT THE BEST PRICES IN BOQUETE"
"OCTOBERS INSIDER PICKS"
"TOP DESTINATIONS"
and spread them in four sections side-by-side near the bottom of the page.

Overall I would like to see the finished product to be something LIKE KMT's and FleetStrides.

WE NEED ONLINE PAYMENT OPTIONS LIKE NORVEX'S WEBSITE HAS

This will be a desktop website but should be very mobile friendly as well.

-rodwell

P.S. Good luck!
Updates

If it isn't already too late to change the website name, the name of the website should be "Calmira Mesa". Added Friday, October 9, 2015

What do you guys think the budget should be to win this? Added Saturday, October 10, 2015

www.lunaverde.example is the most amazing simple site. Whoever can make me a replica with my specifications will win immediately!!!! Added Sunday, October 18, 2015

OMG www.lunaverde.example is the bomb!So simple and elegant. Whoever can make me an EXACT REPLICA OF WWW.LUNAVERDE.EXAMPLE as my site with the specifications mentioned in my brief will take home the $825.00 immediately! Good luck amigos! Added Sunday, October 18, 2015

Does anybody know how to add recurring monthly billing options on this website? Added Sunday, October 18, 2015

Target Market(s)

ALL MARKETS

Industry/Entity Type

Product

Coding

Coded - Design and coding required

Number of Pages Required

5+ page

Requirements
Must have
• Coinlark payment options.
• I must be able to add and remove photos/text and video from the HTML files in the page.
• Be creative my friends, and may the odds be forever in your favor!
Nice to have
• I added some photos of a good layout for our page below.

```html
<!DOCTYPE html>
<html lang="en">
<head>
<meta charset="utf-8">
<title>Calmira Mesa — Travel &amp; Local Guide</title>
<link href="https://fonts.googleapis.com/css2?family=Lato:wght@300;400;700;900&family=Open+Sans:wght@400;600;700&display=swap" rel="stylesheet">
<style>
:root{
  --blue:#1e88e5;
  --blue-dark:#1565c0;
  --ink:#2b2f33;
  --muted:#8a9199;
  --line:#e3e7eb;
  --bg:#ffffff;
  --soft:#f4f6f8;
  --footer:#2a2d31;
  --footer-bottom:#1f2124;
  --green:#43a047;
}
*{box-sizing:border-box;margin:0;padding:0}
html,body{width:1200px;height:3124px;overflow:hidden;background:var(--bg)}
body{font-family:"Open Sans",sans-serif;color:var(--ink);font-size:14px;position:relative}
.wrap{width:1080px;margin:0 auto;position:relative}

/* Header */
.site-header{height:48px;background:#fff;border-bottom:1px solid var(--line)}
.site-header .wrap{display:flex;align-items:center;height:48px}
.brand{font-family:"Lato",sans-serif;font-weight:900;font-size:24px;color:var(--blue);display:flex;align-items:center;gap:8px}
.brand-dot{width:12px;height:12px;background:var(--blue);border-radius:50%}
.main-nav{margin-left:auto;display:flex;gap:34px;font-size:12px;color:#555}
.main-nav a{color:inherit;text-decoration:none}
.main-nav a.active{color:var(--blue);font-weight:600}
.search-icon{margin-left:30px}

/* Hero */
.hero{height:432px;background:linear-gradient(180deg,#6fa8c9 0%,#9cc6dc 45%,#4f8fb2 75%,#2c5f80 100%);position:relative;text-align:center;color:#fff}
.hero-eyebrow{position:absolute;top:165px;width:100%;font-family:"Lato",sans-serif;font-size:22px;letter-spacing:8px;font-weight:400}
.hero-title{position:absolute;top:200px;width:100%;font-family:"Lato",sans-serif;font-weight:900;font-size:48px;letter-spacing:1px}
.hero-btn{position:absolute;top:286px;left:50%;transform:translateX(-50%);background:var(--blue);color:#fff;font-size:11px;font-weight:700;padding:10px 24px;border-radius:3px;letter-spacing:1px}
.hero-arrow{position:absolute;top:200px;width:28px;height:64px;background:rgba(0,0,0,.25);display:flex;align-items:center;justify-content:center}
.hero-arrow.left{left:0}.hero-arrow.right{right:0}

/* Tabs + search */
.tabs{height:60px;background:var(--blue)}
.tabs .wrap{display:flex;height:60px;align-items:center;gap:0}
.tab{width:64px;height:60px;display:flex;align-items:center;justify-content:center}
.tab.active{background:var(--blue-dark)}
.search-panel{height:260px;background:#fff;box-shadow:0 2px 6px rgba(0,0,0,.06)}
.search-panel h2{font-family:"Lato",sans-serif;font-weight:700;font-size:30px;padding-top:38px}
.fields{display:flex;gap:24px;margin-top:30px;align-items:flex-end}
.field label{display:block;font-size:13px;color:#555;margin-bottom:8px}
.field .input{height:40px;border:1px solid var(--line);border-radius:3px;font-size:12px;color:var(--muted);display:flex;align-items:center;padding:0 12px;justify-content:space-between}
.find-btn{height:40px;background:var(--blue);color:#fff;font-size:12px;font-weight:700;padding:0 22px;display:flex;align-items:center;border-radius:3px}

/* Destinations */
.dest-heading{text-align:center;font-family:"Lato",sans-serif;font-size:26px;color:#555;margin-top:34px}
.dest-heading b{color:var(--blue);font-weight:700}
.dest-grid{position:relative;height:840px;margin-top:28px}
.tile{position:absolute;color:#fff;overflow:hidden}
.tile .name{position:absolute;left:14px;top:14px;font-family:"Lato",sans-serif;font-size:30px;font-weight:400}
.tile .tag{position:absolute;left:14px;top:54px;font-size:10px;background:rgba(255,255,255,.85);color:#333;padding:2px 6px}
.tile .count{position:absolute;right:14px;bottom:22px;font-family:"Lato",sans-serif;font-size:26px;font-weight:700}
.tile .sub{position:absolute;right:14px;bottom:8px;font-size:10px}
.more-btn{height:60px;background:var(--blue);color:#fff;display:flex;align-items:center;justify-content:center;font-family:"Lato",sans-serif;font-size:20px}

/* Hot trips */
.lower{display:flex;gap:40px;margin-top:60px}
.trips{width:700px}
.trip-tabs{display:flex;gap:26px;border-bottom:2px solid var(--line);font-size:15px;padding-bottom:10px}
.trip-tabs .on{color:var(--blue);font-weight:600;position:relative}
.trip-tabs .on::after{content:"";position:absolute;left:0;right:0;bottom:-12px;height:2px;background:var(--blue)}
.trip{display:flex;height:140px;margin-top:38px;border-bottom:1px solid var(--line)}
.trip .thumb{width:180px;height:120px;flex:none}
.trip .info{flex:1;padding:8px 20px}
.trip .title{font-family:"Lato",sans-serif;font-size:20px;font-weight:700}
.trip .meta{font-size:12px;color:var(--muted);line-height:18px;margin-top:6px}
.trip .rating{display:flex;justify-content:space-between;margin-top:20px;font-size:12px;color:var(--muted)}
.icons{display:flex;gap:12px}
.icons span{width:14px;height:12px;background:#9aa2aa;border-radius:2px}
.trip .price{width:140px;border-left:1px solid var(--line);padding:8px 0 0 22px}
.price small{font-size:11px;color:var(--muted);display:block}
.price b{font-family:"Lato",sans-serif;font-size:30px;color:var(--ink)}
.quick{margin-top:18px;border:1px solid var(--blue);color:var(--blue);font-size:11px;padding:6px 12px;display:inline-block;border-radius:3px}

.why{width:340px}
.why h3{font-family:"Lato",sans-serif;font-weight:400;font-size:36px;line-height:44px;color:var(--blue-dark)}
.perk{display:flex;align-items:center;gap:16px;padding:20px 0;border-bottom:1px solid var(--line)}
.perk .tick{width:32px;height:32px;border:2px solid var(--green);border-radius:50%;flex:none;display:flex;align-items:center;justify-content:center}
.perk b{display:block;font-size:14px}
.perk small{font-size:11px;color:var(--muted)}
.video{margin-top:34px;height:180px;background:linear-gradient(135deg,#d7dde2,#9aa6b0);position:relative}
.video .bar{position:absolute;left:0;right:0;bottom:0;height:28px;background:rgba(0,0,0,.55)}

/* Footer */
.site-footer{position:absolute;top:2652px;left:0;width:1200px;height:428px;background:var(--footer);color:#bfc4c9}
.footer-brand{position:absolute;left:60px;top:0;width:210px;height:310px;background:var(--blue);color:#fff;padding:26px 22px;font-size:12px;line-height:20px}
.footer-brand .brand{color:#fff;font-size:24px;margin-bottom:30px}
.fcol{position:absolute;top:36px;font-size:12px;line-height:20px}
.fcol h4{color:var(--blue);font-family:"Lato",sans-serif;font-size:16px;margin-bottom:14px}
.call small{font-size:13px;color:#ddd;display:block;line-height:20px}
.call .phone{font-family:"Lato",sans-serif;font-size:38px;color:var(--blue);font-weight:400;margin-top:14px}
.social{display:flex;gap:10px;margin-top:22px}
.social span{width:30px;height:30px;border-radius:50%;background:#e53935}
.social span:nth-child(1),.social span:nth-child(2){background:var(--blue)}
.footer-bottom{position:absolute;top:3080px;left:0;width:1200px;height:44px;background:var(--footer-bottom);color:#8a9199;font-size:11px;display:flex;align-items:center;justify-content:center}
</style>
</head>
<body>

<header class="site-header">
  <div class="wrap">
    <div class="brand"><span class="brand-dot"></span>Calmira Mesa</div>
    <nav class="main-nav">
      <a class="active" href="#">Home</a><a href="#">News</a><a href="#">Travel</a><a href="#">Activities</a><a href="#">Shop &amp; Dine</a><a href="#">Store</a><a href="#">More...</a>
    </nav>
    <svg class="search-icon" width="14" height="14" viewBox="0 0 14 14"><circle cx="6" cy="6" r="4.5" fill="none" stroke="#555" stroke-width="1.6"/><line x1="9.3" y1="9.3" x2="13" y2="13" stroke="#555" stroke-width="1.6"/></svg>
  </div>
</header>

<section class="hero" role="img" aria-label="Mountain lake with cable car at dusk">
  <div class="hero-arrow left"><svg width="10" height="16"><path d="M8 1 2 8l6 7" stroke="#fff" stroke-width="2" fill="none"/></svg></div>
  <div class="hero-eyebrow">LAST MINUTE DEAL</div>
  <div class="hero-title">TOP DISCOUNT PARIS HOTELS</div>
  <div class="hero-btn">BOOK NOW</div>
  <div class="hero-arrow right"><svg width="10" height="16"><path d="M2 1l6 7-6 7" stroke="#fff" stroke-width="2" fill="none"/></svg></div>
</section>

<div class="tabs">
  <div class="wrap">
    <div class="tab"><svg width="20" height="20"><circle cx="10" cy="10" r="8" fill="#fff"/></svg></div>
    <div class="tab active"><svg width="18" height="18"><rect x="3" y="2" width="12" height="14" fill="#fff"/></svg></div>
    <div class="tab"><svg width="20" height="16"><rect x="2" y="5" width="16" height="10" fill="#fff"/></svg></div>
    <div class="tab"><svg width="20" height="16"><rect x="2" y="3" width="16" height="10" rx="2" fill="#fff"/></svg></div>
    <div class="tab"><svg width="20" height="16"><rect x="2" y="4" width="16" height="9" fill="#fff"/></svg></div>
  </div>
</div>

<section class="search-panel">
  <div class="wrap">
    <h2>Where would you like to go?</h2>
    <div class="fields">
      <div class="field" style="width:330px"><label>Destinations</label><div class="input">Country, city, airport...<svg width="10" height="14"><path d="M5 1a4 4 0 0 1 4 4c0 3-4 8-4 8S1 8 1 5a4 4 0 0 1 4-4z" fill="var(--blue)"/></svg></div></div>
      <div class="field" style="width:170px"><label>Check in</label><div class="input">Date</div></div>
      <div class="field" style="width:170px"><label>Check out</label><div class="input">Date</div></div>
      <div class="field" style="width:170px"><label>Guest</label><div class="input">all guest ▾</div></div>
      <div class="find-btn">Find My Hotel</div>
    </div>
  </div>
</section>

<main class="wrap">
  <p class="dest-heading">More than <b>238 Destinations</b> is waiting</p>

  <div class="dest-grid">
    <div class="tile" role="img" aria-label="Florence street view" style="left:0;top:0;width:250px;height:258px;background:linear-gradient(135deg,#c9a57a,#7a5a3c)"><span class="name">Florenze</span><span class="tag">Italy</span><span class="count">845</span><span class="sub">available hotel</span></div>
    <div class="tile" role="img" aria-label="Toluca coastline" style="left:276px;top:0;width:250px;height:258px;background:linear-gradient(135deg,#7fb2d8,#3c6e96)"><span class="name">Toluca</span><span class="tag">Mexico</span><span class="count">132</span><span class="sub">available hotel</span></div>
    <div class="tile" role="img" aria-label="Venice resort pool" style="left:552px;top:0;width:528px;height:540px;background:linear-gradient(160deg,#a9c6d6 0%,#5a8cab 45%,#2f6a8c 100%)"><span class="name">Venice</span><span class="tag">Italy</span><span class="count">2341</span><span class="sub">available hotel</span></div>
    <div class="tile" role="img" aria-label="Ohio hillside town by the sea" style="left:0;top:282px;width:250px;height:258px;background:linear-gradient(135deg,#5f97c4,#2f5d82)"><span class="name">Ohio</span><span class="tag">USA</span><span class="count">2531</span><span class="sub">available hotel</span></div>
    <div class="tile" role="img" aria-label="Venice seaside view" style="left:276px;top:282px;width:250px;height:258px;background:linear-gradient(135deg,#8fc0dc,#4d7fa0)"><span class="name">Venice</span><span class="tag">Italy</span><span class="count">2531</span><span class="sub">available hotel</span></div>
    <div class="tile" role="img" aria-label="Maldives villa terrace" style="left:0;top:564px;width:250px;height:276px;background:linear-gradient(135deg,#c8c9c4,#6f7a80)"><span class="name">Maldives</span><span class="tag">Maldives</span><span class="count">2531</span><span class="sub">available hotel</span></div>
    <div class="tile" role="img" aria-label="Istanbul harbour" style="left:276px;top:564px;width:250px;height:276px;background:linear-gradient(135deg,#d7b88c,#8a6a48)"><span class="name">Istanbul</span><span class="tag">Turkey</span><span class="count">2531</span><span class="sub">available hotel</span></div>
    <div class="tile" role="img" aria-label="Bali hotel room" style="left:552px;top:564px;width:250px;height:276px;background:linear-gradient(135deg,#b9ada0,#6a5b4d)"><span class="name">Bali</span><span class="tag">Indonesia</span><span class="count">2531</span><span class="sub">available hotel</span></div>
    <div class="tile" role="img" aria-label="Phu Quoc bedroom" style="left:828px;top:564px;width:252px;height:276px;background:linear-gradient(135deg,#d8c2a6,#8d6f52)"><span class="name">Phu Quoc</span><span class="tag">Vietnam</span><span class="count">2531</span><span class="sub">available hotel</span></div>
  </div>
  <div class="more-btn">More Destinations</div>

  <div class="lower">
    <section class="trips">
      <div class="trip-tabs"><span class="on">Hot trips</span><span>Recent items</span></div>

      <article class="trip">
        <div class="thumb" role="img" aria-label="Poolside city view" style="background:linear-gradient(135deg,#9fd0e6,#4e8fb2)"></div>
        <div class="info"><div class="title">Spectacular City Views</div><div class="meta">4 attractions<br>1 day - 1 night</div><div class="rating"><span>7.4 Good</span><span class="icons"><span></span><span></span><span></span><span></span><span></span></span></div></div>
        <div class="price"><small>adult from</small><b>$200</b><small>per person</small><span class="quick">Quick book</span></div>
      </article>
      <article class="trip">
        <div class="thumb" role="img" aria-label="Flower market stall" style="background:linear-gradient(135deg,#e8a0a8,#a04a5a)"></div>
        <div class="info"><div class="title">Romantic New York</div><div class="meta">4 attractions<br>1 day - 1 night</div><div class="rating"><span>7.4 Good</span><span class="icons"><span></span><span></span><span></span><span></span><span></span></span></div></div>
        <div class="price"><small>adult from</small><b>$200</b><small>per person</small><span class="quick">Quick book</span></div>
      </article>
      <article class="trip">
        <div class="thumb" role="img" aria-label="Hotel room with bed" style="background:linear-gradient(135deg,#c9b3a0,#6e5646)"></div>
        <div class="info"><div class="title">NYC Family Fun Pass - Winter</div><div class="meta">4 attractions<br>1 day - 1 night</div><div class="rating"><span>7.4 Good</span><span class="icons"><span></span><span></span><span></span><span></span><span></span></span></div></div>
        <div class="price"><small>adult from</small><b>$200</b><small>per person</small><span class="quick">Quick book</span></div>
      </article>
      <article class="trip">
        <div class="thumb" role="img" aria-label="Beach with sea and sky" style="background:linear-gradient(180deg,#bfe0ef,#6fb0cf 60%,#e0d2b4)"></div>
        <div class="info"><div class="title">NYC Land &amp; Sea</div><div class="meta">4 attractions<br>1 day - 1 night</div><div class="rating"><span>7.4 Good</span><span class="icons"><span></span><span></span><span></span><span></span><span></span></span></div></div>
        <div class="price"><small>adult from</small><b>$200</b><small>per person</small><span class="quick">Quick book</span></div>
      </article>
    </section>

    <aside class="why">
      <h3>Why your friends like our services?</h3>
      <div class="perk"><span class="tick"><svg width="14" height="12"><path d="M1 6l4 4 8-9" stroke="var(--green)" stroke-width="2" fill="none"/></svg></span><div><b>100,000 real deals</b><small>Best booking rates, every day</small></div></div>
      <div class="perk"><span class="tick"><svg width="14" height="12"><path d="M1 6l4 4 8-9" stroke="var(--green)" stroke-width="2" fill="none"/></svg></span><div><b>100% trusted reviews</b><small>Written by real verified guests</small></div></div>
      <div class="perk"><span class="tick"><svg width="14" height="12"><path d="M1 6l4 4 8-9" stroke="var(--green)" stroke-width="2" fill="none"/></svg></span><div><b>24/7 global support</b><small>We are here whenever you call</small></div></div>
      <div class="perk"><span class="tick"><svg width="14" height="12"><path d="M1 6l4 4 8-9" stroke="var(--green)" stroke-width="2" fill="none"/></svg></span><div><b>24/7 global support</b><small>Help in your own language</small></div></div>
      <div class="perk"><span class="tick"><svg width="14" height="12"><path d="M1 6l4 4 8-9" stroke="var(--green)" stroke-width="2" fill="none"/></svg></span><div><b>Manage your bookings online</b><small>Change plans in a few clicks</small></div></div>
      <div class="video" role="img" aria-label="Video preview of a city skyline"><div class="bar"></div></div>
    </aside>
  </div>
</main>

<footer class="site-footer">
  <div class="footer-brand">
    <div class="brand">Calmira Mesa</div>
    48 Ridge Lane, Alto Verde,<br>Coclé, Panama<br><br>+507 055-210-480<br>hello@calmiramesa.example
  </div>
  <div class="fcol" style="left:330px;width:170px"><h4>About Us</h4>Local guides and listings for the whole mesa, with news, tours and trusted places to stay, eat and shop all year.</div>
  <div class="fcol" style="left:540px"><h4>Categories</h4>Countries<br>Regions<br>Cities<br>Districts<br>Countries<br>Airports<br>Hotels<br>Places of Interest</div>
  <div class="fcol" style="left:720px"><h4>Recent Blog</h4>Countries<br>Regions<br>Cities<br>Districts<br>Countries<br>Airports<br>Hotels<br>Places of Interest</div>
  <div class="fcol call" style="left:900px;width:240px"><small>For Special booking request, please call</small><div class="phone">055-210-480</div><div class="social"><span></span><span></span><span></span><span></span></div></div>
</footer>
<div class="footer-bottom">©2015 Calmira Mesa. All rights reserved.</div>

</body>
</html>
```